依頼詳細
宮城県仙台市に新たにオープンするサロンのチラシの依頼になります。
ビルの1Fには高級時計店、隣のビルは老舗高級百貨店があります。
都会的な洗練されたデザインにしてほしいです。
記載項目

K.A.Z by sorvique
022-614-5027
仙台アーケード街に2022.6.1 NEW OPEN
サイズ
A5
ページ数
両面
希望イメージ
シンプル 複雑
単色 カラフル
暗い 明るい
日常 高級
遊び心 厳粛
未来的 伝統的
女性的 男性的
希望する色
グレー系
納品ファイル
• 高解像度JPG (.jpg)
• フォトショップ形式 (.psd)
補足説明
名刺デザインはミスです
チラシデザインの作成を依頼します。
追加のデータです。
追加データです
以前出店の際に作っていただいたチラシデザインです。
イメージこのような形がいいです。
※マツエクは今回導入しません。
希望カラーをグレーにしましたが、
あまり暗い印象にはしたくありません。

あとスタイル写真複数枚載せてますが、
あまりごちゃごちゃにはしたくないので
人物写真は2〜3枚まででお願いします。

追加データで載せた以前のチラシのイメージで作って欲しいです。
mapも載せて欲しいです。
■ 選んだ理由

全体的にまとまりがあり、おしゃれ可愛さもあり
季節も考えてのカラーバリエーションなどのご提案もあって
とてもよかったです。

■ 提案者全員のお礼・コメント

この度は、弊社のコンペに参加・ご提案いただき誠に有り難うございました。

```html
<!DOCTYPE html>
<html lang="ja">
<head>
<meta charset="utf-8">
<title>K.A.Z by sorvique 美容室 NEW OPEN</title>
<link href="https://fonts.googleapis.com/css2?family=Bodoni+Moda:wght@500;600&family=Noto+Serif+JP:wght@400;600&display=swap" rel="stylesheet">
<style>
  :root {
    --sheet: #ffffff;
    --navy: #1e2846;
    --pink: #d23a6e;
    --frame: #c9c9c9;
    --photo-light: #e4e2df;
    --photo-mid: #cfcbc6;
    --photo-dark: #a9a39d;
    --caption: #555555;
  }
  * { margin: 0; padding: 0; box-sizing: border-box; }
  html, body { width: 848px; height: 1200px; overflow: hidden; background: var(--sheet); }
  .sheet { position: relative; width: 848px; height: 1200px; }
  .file-caption {
    position: absolute; top: 26px; right: 86px;
    font-family: "Noto Serif JP", serif; font-size: 13px; letter-spacing: 0.04em;
    color: var(--caption);
  }
  .flyer {
    position: absolute; left: 79px; top: 108px; width: 691px; height: 982px;
    border: 1px solid var(--frame); overflow: hidden;
  }
  .style-photo {
    position: absolute; inset: 0 0 110px 0;
    background: radial-gradient(ellipse at 62% 55%, var(--photo-dark) 0%, var(--photo-mid) 30%, var(--photo-light) 70%);
  }
  .headline {
    position: absolute; left: 0; right: 0; top: 14px; text-align: center;
    font-family: "Bodoni Moda", serif; font-weight: 500; font-size: 120px;
    letter-spacing: -0.01em; line-height: 1; color: var(--navy);
    white-space: nowrap;
  }
  .open-date {
    position: absolute; right: 30px; top: 104px;
    font-family: "Bodoni Moda", serif; font-weight: 600; font-size: 122px;
    line-height: 1; letter-spacing: 0.02em; color: var(--navy);
    white-space: nowrap;
  }
  .open-date .day { color: var(--pink); }
  .location {
    position: absolute; left: 40px; top: 330px;
    writing-mode: vertical-rl;
    font-family: "Noto Serif JP", serif; font-weight: 600; font-size: 22px;
    letter-spacing: 0.14em; color: var(--navy);
  }
  .salon-name {
    position: absolute; right: 50px; bottom: 126px; text-align: center;
    font-family: "Bodoni Moda", serif; font-weight: 500; font-size: 56px;
    line-height: 1; letter-spacing: 0.04em; color: var(--navy);
  }
  .salon-name small { display: block; font-size: 16px; margin-top: 6px; letter-spacing: 0.06em; }
  .info-band {
    position: absolute; left: 0; right: 0; bottom: 0; height: 110px; background: var(--sheet);
  }
  .brand-dot {
    position: absolute; left: 38px; top: 32px; width: 46px; height: 46px;
    border-radius: 50%; background: var(--navy);
  }
  .offer {
    position: absolute; left: 100px; top: 34px;
    font-family: "Noto Serif JP", serif; font-size: 15px; line-height: 1.5;
    letter-spacing: 0.08em; color: var(--pink);
  }
  .salon-type {
    position: absolute; right: 98px; top: 40px;
    font-family: "Noto Serif JP", serif; font-weight: 600; font-size: 24px;
    letter-spacing: 0.3em; color: var(--navy);
  }
</style>
</head>
<body>
<div class="sheet">
  <p class="file-caption">6月ニューオープン_美容室チラシ_design_omote_Type_B_[elegant_version]</p>
  <section class="flyer">
    <div class="style-photo" role="img" aria-label="ショートヘアの女性の横顔、黒いトップス、グレーの背景のスタイル写真"></div>
    <h1 class="headline">NEWOPEN</h1>
    <p class="open-date">2022.<span class="day">6.1</span></p>
    <p class="location">▼仙台アーケード街にオープン！</p>
    <p class="salon-name">K.A.Z<small>by sorvique</small></p>
    <div class="info-band">
      <span class="brand-dot"></span>
      <p class="offer">このチラシ持参で、<br>トリートメントをプレゼント。</p>
      <p class="salon-type">美容室</p>
    </div>
  </section>
</div>
</body>
</html>
```